Nitrogen generation business website

Project Overview:
This project aims to create a sleek, user-friendly, and responsive WordPress template for Kelbo4, a provider of Nitrogen generation solutions. The site will serve as a primary touchpoint for customers and businesses looking to enquire about or purchase Kelbo4 products and services. The website should clearly communicate the benefits of working with Kelbo4 as a distributor, focusing on ease of access, expert consultation, and fast, reliable service.
Target Audience:
• Industrial companies seeking Nitrogen solutions.
• Engineers, facility managers, and purchasing teams in need of high-quality Nitrogen systems.
• Partners or businesses seeking to collaborate or purchase through a distributor.
Key Objectives:
1. Establish Kelbo4’s Brand Identity: Use the bold, energetic logo and branding of Kelbo4 (as seen in the uploaded logo) throughout the design. Ensure the brand’s personality shines, with a focus on modernity, reliability, and innovation.
2. Showcase Products and Solutions: Display detailed product categories and descriptions, emphasising the solutions Kelbo4 offers.
3. Lead Generation: Incorporate contact forms, quote requests, and easy-to-find CTAs to convert visitors into leads.
4. User-Centric Design: The design must be intuitive and user-friendly, providing a smooth experience across desktop and mobile devices.
Design Requirements:
1. Home Page:
• Hero Banner: A dynamic, visually engaging hero banner featuring air and gas purification systems, paired with strong CTAs like “Request a Quote” or “Contact Us for Solutions.” The banner should align with the vibrant red and yellow tones in the Kelbo4 logo.
• Key Product Categories: Introduce the main product categories with icons or images linked to individual product pages.
• Kelbo4 Expertise Section: A section emphasising the company’s role as a trusted distributor, backed by experience and a strong partnership network.
• Why Choose Kelbo4: Highlight 3-4 major benefits, such as “Quick Delivery,” “Expert Consultation,” and “Innovative Technology.”
• Client Testimonials/Partners: Space for customer feedback, testimonials, or logos of partner companies to build trust.
• Newsletter or Enquiry Form: Place a compact form for capturing visitor details for quotes, enquiries, or subscriptions.
2. Product Pages:
• Category Pages: Create well-structured product category pages (e.g., Air Filtration Systems, Nitrogen Generators) similar to industry-standard designs. Each category page should feature professional imagery, short product descriptions, and links to detail pages.
• Product Detail Pages: Each product page will contain:
• High-quality images of the product.
• Detailed specifications, technical descriptions, and features.
• Options to download datasheets or brochures (PDF format).
• Clear CTAs to request a quote or contact sales.
• Product Comparison Tool (Optional): Allow users to compare multiple products, emphasising key features and specifications.
3. About Kelbo4 Page:
• Provide an overview of Kelbo4’s history, mission, and the value it provides as a leading distributor.
• Highlight industry expertise, the partnership network, and any accolades or certifications.
• Mention any regional advantages or special services (e.g., fast delivery times, on-site consultation).
4. Contact Us Page:
• Clean and Simple Form: Include fields for general inquiries or specific product requests.
• Contact Information: Display the company’s, email address info@kelbo4.co.uk.
5. Additional Functionalities:
• Responsive Design: Ensure the design is fully responsive, optimised for mobile, tablet, and desktop viewing.
• SEO Optimisation: Include best practices for search engine optimization (SEO), including clean URLs, meta tags, and image alt text.
• Fast Loading Speed: Optimise images, scripts, and code for fast loading times to improve user experience.
• Social Media Integration: Provide links to social media profiles (if applicable) and potentially include a feed for recent updates.
• Optional Blog: Create a blog space for sharing industry news, product updates, or educational content to engage with visitors and improve SEO.
Style Guide:
1. Color Palette:
• Use colors consistent with the Kelbo4 logo: Red (#FF0000) and Yellow (#FFD700) as primary colors. Incorporate neutral colors (such as white, gray, or black) for balance and readability.
• Accent colors may be introduced for subtle highlights, but the focus should be on the bold, energetic color scheme of Kelbo4.
2. Typography:
• Primary Font for Headings: A bold, modern sans-serif font that complements the strong branding of Kelbo4.
• Secondary Font for Body Text: Clean, easy-to-read sans-serif or serif font for optimal readability across devices.
• Typography Emphasis: Use large, bold typography for headlines to match the boldness of the logo and brand identity.
3. Imagery:
• Use high-quality industrial and technical imagery that reflects the air and gas purification products Kelbo4 distributes.
• Incorporate imagery showing products in action, e.g., in industrial settings or installations.
• Avoid clutter; ensure images are used to enhance user understanding, not overwhelm.
4. Icons:
• Utilise modern, flat-style icons that align with the clean and professional image of Kelbo4. Icons could represent services such as “Fast Delivery,” “Expert Support,” and “High-Quality Products.”
Functionality Requirements:
1. Content Management System (CMS): Build the site using WordPress for easy content management, allowing Kelbo4 staff to update content, product information, and blog posts.
2. Quote Request Integration: Ensure the site has a functional and easy-to-access “Request a Quote” form that appears on every product and service page.
3. Customer Support Section: Optionally include a section for FAQs, product guides, or a knowledge base to support customers and prospects.
4. Security: Implement SSL encryption and ensure that other security best practices (e.g., spam prevention for forms) are followed.
5. Multilingual Support (Optional): Provide the option to support multiple languages, depending on the regional scope of Kelbo4’s distribution services.
Deliverables:
• WordPress template with a homepage, product pages, about section, and contact page.
• SEO-friendly and responsive design.
• Clear CTAs for lead generation (e.g., “Request a Quote”).
• User-friendly interface for both desktop and mobile devices.
Inspiration/Competitors:
• Competitor Analysis: Research similar distributors in the air and gas purification industry for design inspiration.
• Brand Consistency: Ensure Kelbo4’s bold branding is prominent and differentiates it from competitors.
Food & Beverage manufacturers, Laser Cutting, Electronics manufacturers, General Industrial Manufacturers

```html
<!DOCTYPE html>
<html lang="en">
<head>
<meta charset="UTF-8">
<title>Kelbo4 – Nitrogen Generation Solutions</title>
<link href="https://fonts.googleapis.com/css2?family=Poppins:ital,wght@0,400;0,500;0,600;0,700;0,800;1,600;1,700;1,800;1,900&display=swap" rel="stylesheet">
<style>
:root{
  --red:#ff1f1f;
  --red-deep:#e8161b;
  --yellow:#ffc400;
  --orange:#ff7a12;
  --ink:#111111;
  --text:#4a4a4a;
  --muted:#666;
  --panel:#f2f2f2;
  --dark:#121212;
  --footer:#1e1e1e;
  --white:#ffffff;
}
*{margin:0;padding:0;box-sizing:border-box}
html,body{width:1200px;height:3308px;overflow:hidden}
body{font-family:'Poppins',sans-serif;color:var(--text);background:var(--white);position:relative}
.heading{font-family:'Poppins',sans-serif;font-weight:800;font-style:italic;color:var(--ink);text-transform:uppercase;text-align:center;font-size:40px;line-height:1}
.rule{width:139px;height:7px;margin:0 auto;background:linear-gradient(90deg,var(--red) 0 50%,var(--yellow) 50% 100%)}

/* header */
.site-header{position:absolute;top:0;left:0;width:1200px;height:82px;background:var(--white)}
.brand{position:absolute;left:75px;top:20px;font-weight:800;font-size:38px;line-height:42px;color:var(--red);letter-spacing:-.5px}
.main-nav{position:absolute;right:73px;top:32px;display:flex;gap:38px}
.main-nav a{font-size:14.5px;font-weight:600;font-style:italic;color:#222;text-decoration:none;letter-spacing:.3px}
.main-nav a.active{color:var(--red);border-bottom:2px solid var(--red);padding-bottom:3px}

/* hero */
.hero{position:absolute;top:82px;left:0;width:1200px;height:571px;overflow:hidden}
.hero-photo{position:absolute;inset:0;background:linear-gradient(90deg,#3f5670 0%,#7d8ea3 30%,#a4b0bf 50%,#7e8ea1 70%,#3e536b 100%)}
.hero-shade{position:absolute;inset:0;background:radial-gradient(ellipse at 50% 45%,rgba(20,30,45,.15),rgba(20,30,45,.45))}
.hero-content{position:absolute;left:0;width:1200px;top:124px;text-align:center;color:var(--white)}
.hero-kicker{font-weight:900;font-style:italic;font-size:46px;line-height:50px}
.hero-brand{font-weight:900;font-size:104px;line-height:96px;color:var(--red);margin-top:2px}
.hero-tag{font-weight:800;font-style:italic;font-size:36px;line-height:41px;margin-top:8px}
.btn-quote{display:inline-block;margin-top:32px;width:214px;height:54px;line-height:54px;background:linear-gradient(90deg,var(--red),var(--orange));color:var(--white);font-weight:800;font-style:italic;font-size:17px;text-decoration:none}
.hero-dots{position:absolute;top:528px;left:566px;display:flex;gap:12px}
.hero-dots span{width:9px;height:9px;background:var(--white)}
.hero-dots span.on{background:var(--yellow);border-radius:50%}

/* categories */
.categories{position:absolute;top:653px;left:0;width:1200px;height:612px}
.categories .heading{margin-top:67px}
.categories .rule{margin-top:20px}
.intro{font-size:14px;line-height:25px;color:var(--text);text-align:center;width:880px;margin:36px auto 0}
.cat-grid{position:absolute;top:240px;left:75px;display:flex;gap:28px}
.cat-card{width:242px;text-align:center}
.cat-photo{width:242px;height:272px;background:linear-gradient(180deg,#e6e6e6,#dadada);border:2px solid #cfcfcf}
.cat-card.active .cat-photo{border-color:var(--red)}
.cat-name{margin-top:14px;font-size:16.5px;font-weight:700;font-style:italic;color:#222}

/* expertise */
.expertise{position:absolute;top:1265px;left:0;width:1200px;height:445px;background:linear-gradient(100deg,#ffc20e 0%,#ffa10e 35%,#ff6a16 65%,#ff2a22 100%)}
.expertise .heading{color:var(--white);margin-top:76px}
.expertise .rule{margin-top:20px}
.exp-grid{position:absolute;top:180px;left:75px;display:flex;gap:34px}
.exp-card{width:328px;height:184px;background:var(--white);padding:18px 18px 0 14px}
.exp-head{display:flex;align-items:center;gap:18px}
.exp-icon{width:69px;height:69px;border-radius:50%;background:#fdeee0;display:flex;align-items:center;justify-content:center}
.exp-title{font-size:20px;font-weight:800;font-style:italic;color:#222}
.exp-text{font-size:13.5px;line-height:22.5px;color:var(--text);margin-top:20px}

/* why */
.why{position:absolute;top:1710px;left:0;width:1200px;height:505px}
.why .heading{margin-top:68px}
.why .rule{margin-top:20px}
.why-grid{position:absolute;top:172px;left:75px;display:flex;gap:27px}
.why-card{width:333px;height:258px;background:var(--panel);text-align:center;padding-top:44px}
.why-card.raised{background:#f4f4f4;box-shadow:0 4px 14px rgba(0,0,0,.14)}
.why-title{font-size:19px;font-weight:800;font-style:italic;color:#222;margin-top:20px}
.why-text{font-size:13.5px;line-height:22.5px;margin-top:8px;padding:0 20px}

/* testimonials */
.testimonials{position:absolute;top:2215px;left:0;width:1200px;height:429px;background:var(--dark)}
.testimonials .heading{color:var(--white);margin-top:75px}
.testimonials .rule{margin-top:20px}
.quote{width:780px;margin:30px auto 0;text-align:center;color:var(--white);font-size:19px;line-height:32px}
.author{position:absolute;top:288px;left:503px;display:flex;align-items:center;gap:16px}
.avatar{width:64px;height:64px;background:linear-gradient(180deg,#bfbfbf,#8a8a8a)}
.author-name{font-size:14px;font-weight:800;font-style:italic;color:var(--white)}
.author-co{font-size:13px;color:var(--yellow);margin-top:2px}
.arrow{position:absolute;top:187px}
.arrow.prev{left:117px}
.arrow.next{left:1062px}

/* newsletter */
.newsletter{position:absolute;top:2644px;left:0;width:1200px;height:301px}
.newsletter .heading{margin-top:52px}
.newsletter .rule{margin-top:20px}
.newsletter .intro{margin-top:30px;width:900px}
.signup{position:absolute;top:184px;left:254px;width:693px;height:51px;display:flex;border:1px solid #bdbdbd}
.signup-field{flex:1;font-size:12.5px;color:#222;padding-left:15px;line-height:49px;text-transform:uppercase}
.signup-btn{width:114px;background:var(--red-deep);color:var(--white);font-size:12.5px;font-weight:600;text-align:center;line-height:49px}

/* footer */
.site-footer{position:absolute;top:2945px;left:0;width:1200px;height:363px;background:var(--footer);color:#e6e6e6}
.footer-brand{position:absolute;left:77px;top:120px;font-size:60px;font-weight:800;line-height:60px;color:var(--red)}
.footer-col{position:absolute;top:64px}
.footer-col h4{font-size:15.5px;font-weight:800;font-style:italic;color:var(--yellow);text-transform:uppercase;margin-bottom:8px}
.footer-col ul{list-style:none}
.links li{font-size:13px;line-height:28px}
.cats li{font-size:13px;line-height:32px}
.col-links{left:366px}
.col-cats{left:617px}
.col-contact{left:885px}
.contact-row{display:flex;gap:12px;font-size:13px;line-height:23px;margin-top:4px}
.contact-row svg{flex:none;margin-top:5px}
.social{display:flex;gap:20px;margin-top:36px}
.social span{width:20px;height:20px;border-radius:50%;background:#f0f0f0}
.copyright{position:absolute;left:0;bottom:0;width:1200px;height:58px;border-top:1px solid #2e2e2e;text-align:center;line-height:58px;font-size:12.5px;color:#bdbdbd}
</style>
</head>
<body>

<header class="site-header">
  <div class="brand">Kelbo4</div>
  <nav class="main-nav">
    <a class="active" href="#">HOME</a>
    <a href="#">PRODUCTS</a>
    <a href="#">ABOUT KELBO4</a>
    <a href="#">SERVICES</a>
    <a href="#">INDUSTRIES</a>
    <a href="#">BLOG</a>
    <a href="#">CONTACT US</a>
  </nav>
</header>

<section class="hero">
  <div class="hero-photo" role="img" aria-label="Industrial plant room with rows of gas purification vessels and pipework"></div>
  <div class="hero-shade"></div>
  <div class="hero-content">
    <div class="hero-kicker">WELCOME TO</div>
    <div class="hero-brand">KELBO4</div>
    <div class="hero-tag">We are a provider of Nitrogen<br>generation solutions.</div>
    <a class="btn-quote" href="#">REQUEST A QUOTE</a>
  </div>
  <div class="hero-dots"><span class="on"></span><span></span><span></span><span></span></div>
</section>

<section class="categories">
  <h2 class="heading">Product Categories</h2>
  <div class="rule"></div>
  <p class="intro">Sed ut perspiciatis unde omnis iste natus error sit voluptatem accusantium doloremque laudantium, totam rem aperiam, eaque ipsa quae ab illo inventore veritatis et quasi architecto beatae vitae dicta sunt explicabo.</p>
  <div class="cat-grid">
    <div class="cat-card active"><div class="cat-photo" role="img" aria-label="Air filtration system with twin vessels"></div><div class="cat-name">AIR FILTRATION SYSTEMS</div></div>
    <div class="cat-card"><div class="cat-photo" role="img" aria-label="Two nitrogen generator units"></div><div class="cat-name">NITROGEN GENERATORS</div></div>
    <div class="cat-card"><div class="cat-photo" role="img" aria-label="Pre-treatment dryer unit"></div><div class="cat-name">PRE-TREATMENT</div></div>
    <div class="cat-card"><div class="cat-photo" role="img" aria-label="Inline filters and sensor cartridges"></div><div class="cat-name">SENSORS</div></div>
  </div>
</section>

<section class="expertise" role="img" aria-label="Blurred industrial equipment in warm yellow to red tones">
  <h2 class="heading">Kelbo4 Expertise</h2>
  <div class="rule"></div>
  <div class="exp-grid">
    <div class="exp-card">
      <div class="exp-head">
        <div class="exp-icon"><svg width="34" height="34" viewBox="0 0 34 34" fill="none" stroke="#ff2a1f" stroke-width="1.8"><circle cx="17" cy="10" r="5"/><path d="M7 30c0-6 4-10 10-10s10 4 10 10"/><path d="M25 6h6v5h-4l-2 2z"/></svg></div>
        <div class="exp-title">CONSULTATION</div>
      </div>
      <p class="exp-text">Sed ut perspiciatis unde omnis iste natus error sit voluptatem accusantium do loremque laudantium.</p>
    </div>
    <div class="exp-card">
      <div class="exp-head">
        <div class="exp-icon"><svg width="34" height="34" viewBox="0 0 34 34" fill="none" stroke="#ff2a1f" stroke-width="1.8"><path d="M9 12a8 8 0 0 1 16 0z"/><circle cx="17" cy="16" r="5"/><path d="M7 31c0-6 4-9 10-9s10 3 10 9"/><path d="M28 8v14"/></svg></div>
        <div class="exp-title">INSTALLATION</div>
      </div>
      <p class="exp-text">Sed ut perspiciatis unde omnis iste natus error sit voluptatem accusantium do loremque laudantium.</p>
    </div>
    <div class="exp-card">
      <div class="exp-head">
        <div class="exp-icon"><svg width="34" height="34" viewBox="0 0 34 34" fill="none" stroke="#ff2a1f" stroke-width="1.8"><rect x="7" y="5" width="18" height="24" rx="2"/><path d="M11 11h10M11 16h10M11 21h6"/><path d="M24 20l6 6-3 3-6-6z"/></svg></div>
        <div class="exp-title">MAINTENANCE</div>
      </div>
      <p class="exp-text">Sed ut perspiciatis unde omnis iste natus error sit voluptatem accusantium do loremque laudantium.</p>
    </div>
  </div>
</section>

<section class="why">
  <h2 class="heading">Why Choose Kelbo4</h2>
  <div class="rule"></div>
  <div class="why-grid">
    <div class="why-card">
      <svg width="52" height="52" viewBox="0 0 52 52" fill="none" stroke="#ee1c24" stroke-width="4"><circle cx="26" cy="26" r="22"/><path d="M26 13v14l9 6"/></svg>
      <div class="why-title">QUICK DELIVERY</div>
      <p class="why-text">Sed ut perspiciatis unde omnis iste natus error sit voluptatem accusantium do loremque laudantium.</p>
    </div>
    <div class="why-card raised">
      <svg width="60" height="52" viewBox="0 0 60 52" fill="none" stroke="#ee1c24" stroke-width="3.5"><path d="M24 4C12 4 3 11 3 20c0 5 3 9 7 12l-3 9 10-6c2 1 5 1 7 1 12 0 21-7 21-16S36 4 24 4z"/><path d="M45 16c7 3 12 8 12 14 0 4-2 7-5 9l2 8-8-5c-2 1-4 1-6 1-6 0-11-2-14-6"/></svg>
      <div class="why-title">EXPERT CONSULTATION</div>
      <p class="why-text">Sed ut perspiciatis unde omnis iste natus error sit voluptatem accusantium do loremque laudantium.</p>
    </div>
    <div class="why-card">
      <svg width="40" height="54" viewBox="0 0 40 54" fill="none" stroke="#ee1c24" stroke-width="3.5"><path d="M20 3C10 3 4 10 4 19c0 7 4 11 7 15 2 3 2 6 2 7h14c0-1 0-4 2-7 3-4 7-8 7-15C36 10 30 3 20 3z"/><path d="M13 46h14M15 51h10"/></svg>
      <div class="why-title">INNOVATIVE TECHNOLOGY</div>
      <p class="why-text">Sed ut perspiciatis unde omnis iste natus error sit voluptatem accusantium do loremque laudantium.</p>
    </div>
  </div>
</section>

<section class="testimonials">
  <h2 class="heading">Client Testimonials</h2>
  <div class="rule"></div>
  <p class="quote">“Sed ut perspiciatis unde omnis iste natus error sit voluptatem accusantium doloremque laudantium, totam rem aperiam, eaque ipsa quae ab illo inventore veritatis et quasi architecto beatae vitae dicta sunt explicabo.”</p>
  <svg class="arrow prev" width="22" height="34" viewBox="0 0 22 34" fill="none" stroke="#ffffff" stroke-width="2.5"><path d="M18 3L4 17l14 14"/></svg>
  <svg class="arrow next" width="22" height="34" viewBox="0 0 22 34" fill="none" stroke="#ffc400" stroke-width="2.5"><path d="M4 3l14 14L4 31"/></svg>
  <div class="author">
    <div class="avatar" role="img" aria-label="Client portrait"></div>
    <div><div class="author-name">NAME HEADING</div><div class="author-co">Company</div></div>
  </div>
</section>

<section class="newsletter">
  <h2 class="heading">Newsletter Sign Up</h2>
  <div class="rule"></div>
  <p class="intro">Sed ut perspiciatis unde omnis iste natus error sit voluptatem accusantium doloremque laudantium, totam rem aperiam.</p>
  <div class="signup">
    <div class="signup-field">Enter Email Address</div>
    <div class="signup-btn">SIGN UP</div>
  </div>
</section>

<footer class="site-footer">
  <div class="footer-brand">Kelbo4</div>
  <div class="footer-col col-links">
    <h4>Quick Links</h4>
    <ul class="links"><li>Home</li><li>Products</li><li>About Kelbo4</li><li>Services</li><li>Industries</li><li>Blog</li><li>Contact Us</li></ul>
  </div>
  <div class="footer-col col-cats">
    <h4>Categories</h4>
    <ul class="cats"><li>Air Filtration Systems</li><li>Nitrogen Generators</li><li>Pre-Treatment</li><li>Sensors</li></ul>
  </div>
  <div class="footer-col col-contact">
    <h4>Contact Info</h4>
    <div class="contact-row"><svg width="14" height="14" viewBox="0 0 14 14" fill="#ffc400"><path d="M7 0a5 5 0 0 0-5 5c0 4 5 9 5 9s5-5 5-9a5 5 0 0 0-5-5zm0 7a2 2 0 1 1 0-4 2 2 0 0 1 0 4z"/></svg><span>48 Harbour Lane Unit 12,<br>Leeds LS1 4AB, United Kingdom</span></div>
    <div class="contact-row"><svg width="14" height="14" viewBox="0 0 14 14" fill="#ffc400"><path d="M3 1l2 3-1 2c1 2 2 3 4 4l2-1 3 2-1 2C6 14 0 8 1 2z"/></svg><span>+144-555-0100</span></div>
    <div class="contact-row"><svg width="14" height="12" viewBox="0 0 14 12" fill="#ffc400"><path d="M0 1h14v1L7 7 0 2zM0 4l7 5 7-5v8H0z"/></svg><span>info@kelbo4.co.uk</span></div>
    <div class="social" aria-label="Social media links"><span></span><span></span><span></span><span></span><span></span></div>
  </div>
  <div class="copyright">Copyright 2024 © Kelbo4 All Right Reserved</div>
</footer>

</body>
</html>
```